Business Card Re-Design for a Lighting Designer

I would like my business card re-designed. It is currently high gloss and they scratch too easily. I don not think the current design lends itself well to a matte finish. I have included the current design for reference along with our company logo.
Check out our website for current branding.
http://www.brambleorchidstudio.example

Updates
Some of the top contenders are muslim and it is a holiday for them. I do not want to discriminate and would expect the same courtesy for holidays we celebrate.
Target Market(s)
Interior Designers, Architects
Contact Information for Business Card
Logo - Name, Title, Address, Telephone Number and Extension, Email
Font styles to use
Requirements
Must have
- All the information listed on the current business card. If you use Red, it needs to be the red from our logo.
Nice to have
- Vertical and Horizontal Designs will be entertained.
Should not have
- Requirements for a glossy finish...should not look too corporate since we are a design firm.

```html
<!DOCTYPE html>
<html lang="en">
<head>
<meta charset="utf-8">
<title>Bramble Orchid Studio — Business Card</title>
<link rel="stylesheet" href="https://fonts.googleapis.com/css2?family=Jost:wght@300&family=Roboto+Condensed:wght@300;400;700&display=swap">
<style>
  :root {
    --backdrop: #bdb5a3;
    --brand-red: #981a1e;
    --paper: #ffffff;
    --ink: #111111;
    --grey: #8f8f8f;
    --rule: #d7a197;
  }
  * { margin: 0; padding: 0; box-sizing: border-box; }
  html, body { width: 1200px; height: 960px; overflow: hidden; }
  body { background: var(--backdrop); position: relative; }

  .card {
    position: absolute;
    top: 153px;
    width: 364px;
    height: 737px;
    overflow: hidden;
  }
  .card--front { left: 234px; background: var(--paper); }
  .card--back  {
    left: 623px;
    background: var(--brand-red);
    color: var(--paper);
    font-family: "Roboto Condensed", Arial, sans-serif;
    font-weight: 300;
    text-align: center;
  }

  .front__artwork {
    position: absolute;
    left: 0; top: 0;
    width: 364px; height: 414px;
    background: linear-gradient(180deg, var(--brand-red) 0%, #a22328 100%);
  }
  .front__name {
    position: absolute;
    left: 19px; top: 424px;
    font-family: "Jost", Arial, sans-serif;
    font-weight: 300;
    font-size: 50px;
    line-height: 50px;
    color: var(--ink);
    text-transform: uppercase;
  }
  .front__rule {
    position: absolute;
    left: 19px; top: 588px;
    width: 322px; height: 1.5px;
    background: var(--rule);
  }
  .front__tagline {
    position: absolute;
    left: 19px; top: 598px;
    font-family: "Jost", Arial, sans-serif;
    font-weight: 300;
    font-size: 18.5px;
    letter-spacing: 1.6px;
    color: var(--grey);
    white-space: nowrap;
  }

  .back__person { position: absolute; left: 0; right: 0; top: 220px; }
  .back__name { font-size: 40px; line-height: 44px; letter-spacing: -1px; }
  .back__title {
    margin-top: 6px;
    font-weight: 700;
    font-size: 16px;
    letter-spacing: 2.4px;
  }
  .back__details {
    position: absolute; left: 0; right: 0; top: 330px;
    font-size: 17px; line-height: 20px; letter-spacing: -0.3px;
  }
  .back__details p + p { margin-top: 20px; }
  .back__web {
    position: absolute; left: 0; right: 0; top: 474px;
    font-weight: 700; font-size: 17px; letter-spacing: -0.2px;
  }
</style>
</head>
<body>
  <section class="card card--front">
    <div class="front__artwork" role="img" aria-label="Illustration of a spotlight beam falling into a red room drawn in white lines"></div>
    <div class="front__name">Bramble<br>Orchid<br>Studio</div>
    <div class="front__rule"></div>
    <div class="front__tagline">LIGHTING FOR ARCHITECTURE</div>
  </section>

  <section class="card card--back">
    <div class="back__person">
      <h1 class="back__name">MAREN HOLLOWAY</h1>
      <div class="back__title">- PRINCIPAL -</div>
    </div>
    <div class="back__details">
      <p>512 Larkspur Lane, Suite 40<br>Fairhaven, Oregon 97024 USA</p>
      <p>maren@brambleorchidstudio.example<br>555.014.2286 x1</p>
    </div>
    <div class="back__web">www.brambleorchidstudio.example</div>
  </section>
</body>
</html>
```